Ombu Crate branding

Business branding package for our concept Ombu Crate, including logo, stationary, business card, website and branding guide/branding strategy.

Target Market(s)

Fish farmers and investors

Industry/Entity Type

Business

Contact Information for Business Card

See attachment

Logo Text

Ombu Crate

Number of Pages Required

5+ page

Font styles to use
Serif
Sans Serif

```html
<!DOCTYPE html>
<html lang="en">
<head>
<meta charset="utf-8">
<title>Tidewell Marine</title>
<link href="https://fonts.googleapis.com/css2?family=Roboto+Condensed:wght@400;700&family=Roboto:wght@400;500;700&display=swap" rel="stylesheet">
<style>
:root{
  --navy:#0c3a7c;
  --navy-deep:#0a2f66;
  --ink:#2d2d2d;
  --muted:#8a8a8a;
  --nav:#3a3a3a;
  --paper:#f2f2f2;
  --white:#ffffff;
}
*{margin:0;padding:0;box-sizing:border-box}
html,body{width:1200px;height:2514px;overflow:hidden;background:var(--white)}
body{position:relative;font-family:"Roboto",Arial,sans-serif;color:var(--ink)}
.abs{position:absolute}

/* header */
.site-header{left:0;top:0;width:1200px;height:104px;background:var(--white);z-index:5}
.brand{left:87px;top:40px;display:flex;align-items:center;gap:12px}
.brand-dot{width:22px;height:22px;border-radius:50%;background:var(--navy)}
.brand-name{font-family:"Roboto",Arial,sans-serif;font-weight:500;font-size:22px;color:var(--navy);letter-spacing:.3px}
.main-nav{left:536px;top:52px}
.main-nav a{position:absolute;top:0;font-size:15px;color:var(--nav);text-decoration:none;white-space:nowrap}
.main-nav a.active{color:var(--navy);font-weight:500}
.nav-mark{left:540px;top:78px;width:30px;height:20px}

/* hero */
.hero{left:0;top:104px;width:1200px;height:570px;background:linear-gradient(180deg,#0f7fe0 0%,#1a8ff0 25%,#0e5fbf 60%,#0b4a9a 80%,#1a7fc8 100%)}
.hero-title{left:0;top:308px;width:1200px;text-align:center;font-family:"Roboto Condensed","Arial Narrow",sans-serif;font-weight:700;font-size:40px;color:var(--white);letter-spacing:.5px}
.hero-text{left:295px;top:368px;width:610px;text-align:center;font-size:13px;line-height:20px;color:var(--white)}
.btn-outline{left:549px;top:429px;width:103px;height:37px;border:2px solid var(--white);border-radius:3px;color:var(--white);font-size:13px;font-weight:500;display:flex;align-items:center;justify-content:center}
.hero-arrow{top:366px;width:24px;height:40px}

/* company */
.company{left:0;top:640px;width:1200px;height:460px}
.section-title{font-family:"Roboto Condensed","Arial Narrow",sans-serif;font-size:25px;color:var(--ink);font-weight:400}
.company-title{left:87px;top:765px}
.company-text{left:87px;top:808px;width:540px;font-size:13px;line-height:20px;color:var(--muted);text-align:justify}
.btn-solid{left:89px;top:949px;width:104px;height:43px;background:var(--navy);color:var(--white);border-radius:3px;font-size:13px;font-weight:500;display:flex;align-items:center;justify-content:center;box-shadow:2px 2px 0 #5b7fb5}
.company-figure{left:687px;top:746px;width:423px;height:271px;border:4px solid #d7282c;background:linear-gradient(180deg,#e7b9bd 0%,#d6a3a8 100%)}

/* services */
.services-band{left:0;top:1070px;width:1200px;height:570px}
.services-title{left:0;top:1188px;width:1200px;text-align:center}
.service{width:240px;text-align:center}
.service-hex{display:block;margin:0 auto;width:117px;height:122px}
.service-name{margin-top:20px;font-size:15px;font-weight:500;color:var(--ink)}
.service-text{margin:6px auto 0;width:210px;font-size:12px;line-height:18px;color:#7e8ea3}
.service-more{margin-top:8px;font-size:11px;font-weight:700;color:var(--navy-deep)}

/* news */
.news-title{left:0;top:1668px;width:1200px;text-align:center}
.news-mark{left:583px;top:1712px;width:34px;height:20px}
.news-card{top:1777px;width:233px}
.news-photo{position:relative;width:233px;height:213px;border-radius:4px;overflow:hidden}
.news-date{position:absolute;left:0;bottom:0;width:100%;height:34px;background:rgba(13,52,110,.72);color:var(--white);font-size:14px;font-weight:700;text-align:right;padding:9px 8px 0 0}
.news-head{margin-top:16px;font-size:14px;font-weight:700;color:var(--ink)}
.news-text{margin-top:6px;font-size:12px;line-height:17px;color:#6f6f6f;width:215px}
.news-link{margin-top:6px;font-size:12px;font-weight:700;color:var(--navy-deep)}

/* footer */
.footer-bg{left:0;top:2130px;width:1200px;height:384px}
.footer-col{top:2243px}
.footer-head{font-family:"Roboto Condensed","Arial Narrow",sans-serif;font-size:20px;color:var(--white);margin-bottom:12px}
.footer-list{list-style:none}
.footer-list li{font-size:13px;color:var(--white);height:22.6px;display:flex;align-items:center;gap:14px}
.footer-list.services li{height:26px}
.chev{width:10px;height:8px}
.social li{height:38px;gap:10px}
.social-dot{width:28px;height:28px;border-radius:50%;border:1.5px solid rgba(255,255,255,.8)}
.news-input{left:763px;top:2286px;width:298px;height:37px;border:1px solid rgba(255,255,255,.85);border-radius:3px;font-size:11px;color:var(--white);padding:11px 0 0 14px}
.btn-subscribe{left:763px;top:2335px;width:99px;height:37px;background:var(--navy-deep);color:var(--white);font-size:13px;font-weight:500;display:flex;align-items:center;justify-content:center;border-radius:2px}
.footer-rule{left:87px;top:2444px;width:1026px;height:1px;background:rgba(255,255,255,.45)}
.copyright{left:0;top:2468px;width:1200px;text-align:center;font-size:12px;color:var(--white)}
</style>
</head>
<body>

<header class="site-header abs">
  <div class="brand abs">
    <span class="brand-dot"></span>
    <span class="brand-name">Tidewell Marine</span>
  </div>
  <nav class="main-nav abs">
    <a class="active" style="left:0">HOME</a>
    <a style="left:79px">VISION</a>
    <a style="left:162px">GOALS</a>
    <a style="left:244px">BRANDING</a>
    <a style="left:354px">INFORMATION</a>
    <a style="left:490px">CONTACT US</a>
  </nav>
  <svg class="nav-mark abs" viewBox="0 0 30 20"><path d="M2 12 Q15 22 28 8" fill="none" stroke="#0c3a7c" stroke-width="2.5" stroke-linecap="round"/></svg>
</header>

<section class="hero abs" role="img" aria-label="Underwater photograph of sunlit blue sea above a coral reef"></section>
<svg class="hero-arrow abs" style="left:62px" viewBox="0 0 24 40"><path d="M20 3 L4 20 L20 37" fill="none" stroke="rgba(255,255,255,.6)" stroke-width="2"/></svg>
<svg class="hero-arrow abs" style="left:1112px" viewBox="0 0 24 40"><path d="M4 3 L20 20 L4 37" fill="none" stroke="rgba(255,255,255,.6)" stroke-width="2"/></svg>
<h1 class="hero-title abs">TIDEWELL MARINE</h1>
<p class="hero-text abs">Tidewell Marine will be a provider of aquaculture technology for fish farming in an offshore environment which is the main foundation for the development of Ombu Crate concept</p>
<div class="btn-outline abs">READ MORE</div>

<svg class="company abs" viewBox="0 0 1200 460" preserveAspectRatio="none">
  <path d="M0 10 L400 -28 L755 5 L915 -28 L1200 30 L1200 460 L0 460 Z" fill="#f2f2f2"/>
  <path d="M0 10 L400 -28 L755 5 L915 -28 L1200 30" fill="none" stroke="#7fb8ee" stroke-width="4"/>
</svg>
<h2 class="section-title company-title abs">COMPANY AND GOALS</h2>
<p class="company-text abs">Tidewell Marine was established on September 3rd, 2015. The group behind Tidewell Marine has resources with great experience in engineering and construction of offshore installations for the oil and gas industry as well as the construction of rigs and other structures. It has delivered rig solutions to Norwegian and 15 years. for the global market. The experience within project development and implementation gained from oil related business shall be transferred into the fish farming industry.</p>
<div class="btn-solid abs">READ MORE</div>
<div class="company-figure abs" role="img" aria-label="Rendering of an offshore fish farming rig with a red frame above a net pen"></div>

<svg class="services-band abs" viewBox="0 0 1200 570" preserveAspectRatio="none" role="img" aria-label="Light blue band with a faint water splash">
  <defs><linearGradient id="bandFill" x1="0" y1="0" x2="0" y2="1"><stop offset="0" stop-color="#a6d0fa"/><stop offset="1" stop-color="#b3d8fc"/></linearGradient></defs>
  <path d="M0 12 L330 42 L740 26 L1200 0 L1200 525 L830 520 L660 498 L420 555 L0 510 Z" fill="url(#bandFill)"/>
</svg>
<h2 class="section-title services-title abs">OUR MAIN SERVICES</h2>

<div class="service abs" style="left:192px;top:1270px">
  <svg class="service-hex" viewBox="0 0 117 122"><polygon points="58.5,3 112,32 112,90 58.5,119 5,90 5,32" fill="none" stroke="#fff" stroke-width="2"/><polygon points="58.5,11 105,36 105,86 58.5,111 12,86 12,36" fill="#0c3a7c"/><g stroke="#fff" stroke-width="2.5" fill="none" stroke-linecap="round"><path d="M44 78 V52"/><path d="M58 78 V46"/><path d="M72 78 V52"/><path d="M44 62 L38 56 M44 58 L50 52 M58 58 L52 52 M58 54 L64 48 M72 62 L78 56 M72 58 L66 52"/></g></svg>
  <div class="service-name">LOREM IPSUM</div>
  <div class="service-text">When an unknown printer galley of type and scrambled</div>
  <div class="service-more">READ MORE &gt;&gt;</div>
</div>
<div class="service abs" style="left:480px;top:1270px">
  <svg class="service-hex" viewBox="0 0 117 122"><polygon points="58.5,3 112,32 112,90 58.5,119 5,90 5,32" fill="none" stroke="#fff" stroke-width="2"/><polygon points="58.5,11 105,36 105,86 58.5,111 12,86 12,36" fill="#0c3a7c"/><ellipse cx="56" cy="61" rx="15" ry="10" fill="#fff"/><polygon points="70,61 82,52 82,70" fill="#fff"/><circle cx="49" cy="59" r="2" fill="#0c3a7c"/></svg>
  <div class="service-name">CONTENT HERE</div>
  <div class="service-text">When an unknown printer galley of type and scrambled</div>
  <div class="service-more">READ MORE &gt;&gt;</div>
</div>
<div class="service abs" style="left:767px;top:1270px">
  <svg class="service-hex" viewBox="0 0 117 122"><polygon points="58.5,3 112,32 112,90 58.5,119 5,90 5,32" fill="none" stroke="#fff" stroke-width="2"/><polygon points="58.5,11 105,36 105,86 58.5,111 12,86 12,36" fill="#0c3a7c"/><rect x="42" y="46" width="33" height="7" fill="#fff"/><rect x="45" y="55" width="27" height="22" fill="#fff"/><rect x="53" y="60" width="11" height="4" fill="#0c3a7c"/></svg>
  <div class="service-name">DOLOR SIT AMET</div>
  <div class="service-text">When an unknown printer galley of type and scrambled</div>
  <div class="service-more">READ MORE &gt;&gt;</div>
</div>

<h2 class="section-title news-title abs">OUR LATEST NEWS</h2>
<svg class="news-mark abs" viewBox="0 0 34 20"><path d="M2 10 Q17 22 32 6" fill="none" stroke="#6fa6dc" stroke-width="2.5" stroke-linecap="round"/></svg>

<article class="news-card abs" style="left:86px">
  <div class="news-photo" role="img" aria-label="Photograph of a child watching fish at an aquarium" style="background:linear-gradient(160deg,#2f8f88,#1e5f6a 60%,#3a7d6e)"><div class="news-date">NOVEMBER 10,2016</div></div>
  <div class="news-head">DOLOR SIT AMET</div>
  <div class="news-text">Lorem Ipsum used since eproduced below for those interested</div>
  <div class="news-link">Click here &gt;&gt;</div>
</article>
<article class="news-card abs" style="left:350px">
  <div class="news-photo" role="img" aria-label="Photograph of a goldfish leaping between two glass bowls" style="background:linear-gradient(180deg,#e8f4fb,#7fc6e6 60%,#1f8fc7)"><div class="news-date">NOVEMBER 11,2016</div></div>
  <div class="news-head">FINIBUS BONORUM</div>
  <div class="news-text">Lorem Ipsum used since eproduced below for those interested</div>
  <div class="news-link">Click here &gt;&gt;</div>
</article>
<article class="news-card abs" style="left:613px">
  <div class="news-photo" role="img" aria-label="Photograph of visitors before a large aquarium tank" style="background:linear-gradient(180deg,#5d86c0,#2c4f8e 60%,#1a2f5a)"><div class="news-date">DECEMBER 27,2016</div></div>
  <div class="news-head">DOLOR SIT AMET</div>
  <div class="news-text">Lorem Ipsum used since eproduced below for those interested</div>
  <div class="news-link">Click here &gt;&gt;</div>
</article>
<article class="news-card abs" style="left:877px">
  <div class="news-photo" role="img" aria-label="Photograph of a parent and child pointing at an aquarium" style="background:linear-gradient(160deg,#2c6e8a,#4a7a7c 50%,#2a4f6a)"><div class="news-date">JANUARY 01,2017</div></div>
  <div class="news-head">DOLOR ET MALORUM</div>
  <div class="news-text">Lorem Ipsum used since eproduced below for those interested</div>
  <div class="news-link">Click here &gt;&gt;</div>
</article>

<svg class="footer-bg abs" viewBox="0 0 1200 384" preserveAspectRatio="none" role="img" aria-label="Deep blue water backdrop with a fish and a glass bowl">
  <defs><linearGradient id="footFill" x1="0" y1="0" x2="0" y2="1"><stop offset="0" stop-color="#1f5ea6"/><stop offset="1" stop-color="#174a8a"/></linearGradient></defs>
  <path d="M0 20 L420 58 L800 30 L1200 8 L1200 384 L0 384 Z" fill="url(#footFill)"/>
  <path d="M0 20 L420 58 L800 30 L1200 8" fill="none" stroke="#8cc0ef" stroke-width="5"/>
</svg>

<div class="footer-col abs" style="left:137px">
  <div class="footer-head">QUICK LINKS</div>
  <ul class="footer-list">
    <li><svg class="chev" viewBox="0 0 10 8"><path d="M1 1 L4 4 L1 7 M5 1 L8 4 L5 7" stroke="#fff" fill="none" stroke-width="1.3"/></svg>Home</li>
    <li><svg class="chev" viewBox="0 0 10 8"><path d="M1 1 L4 4 L1 7 M5 1 L8 4 L5 7" stroke="#fff" fill="none" stroke-width="1.3"/></svg>Vision</li>
    <li><svg class="chev" viewBox="0 0 10 8"><path d="M1 1 L4 4 L1 7 M5 1 L8 4 L5 7" stroke="#fff" fill="none" stroke-width="1.3"/></svg>Goals</li>
    <li><svg class="chev" viewBox="0 0 10 8"><path d="M1 1 L4 4 L1 7 M5 1 L8 4 L5 7" stroke="#fff" fill="none" stroke-width="1.3"/></svg>Branding</li>
    <li><svg class="chev" viewBox="0 0 10 8"><path d="M1 1 L4 4 L1 7 M5 1 L8 4 L5 7" stroke="#fff" fill="none" stroke-width="1.3"/></svg>information</li>
    <li><svg class="chev" viewBox="0 0 10 8"><path d="M1 1 L4 4 L1 7 M5 1 L8 4 L5 7" stroke="#fff" fill="none" stroke-width="1.3"/></svg>Contact us</li>
  </ul>
</div>
<div class="footer-col abs" style="left:345px">
  <div class="footer-head">SERVICES</div>
  <ul class="footer-list services">
    <li><svg class="chev" viewBox="0 0 10 8"><path d="M1 1 L4 4 L1 7 M5 1 L8 4 L5 7" stroke="#fff" fill="none" stroke-width="1.3"/></svg>Et Malorum</li>
    <li><svg class="chev" viewBox="0 0 10 8"><path d="M1 1 L4 4 L1 7 M5 1 L8 4 L5 7" stroke="#fff" fill="none" stroke-width="1.3"/></svg>Lorem Ipsum</li>
    <li><svg class="chev" viewBox="0 0 10 8"><path d="M1 1 L4 4 L1 7 M5 1 L8 4 L5 7" stroke="#fff" fill="none" stroke-width="1.3"/></svg>Cicero are also</li>
    <li><svg class="chev" viewBox="0 0 10 8"><path d="M1 1 L4 4 L1 7 M5 1 L8 4 L5 7" stroke="#fff" fill="none" stroke-width="1.3"/></svg>Standard chunk</li>
    <li><svg class="chev" viewBox="0 0 10 8"><path d="M1 1 L4 4 L1 7 M5 1 L8 4 L5 7" stroke="#fff" fill="none" stroke-width="1.3"/></svg>Theory of ethics</li>
  </ul>
</div>
<div class="footer-col abs" style="left:563px">
  <div class="footer-head">FOLLOW US</div>
  <ul class="footer-list social">
    <li><span class="social-dot"></span>Friendline</li>
    <li><span class="social-dot"></span>Chirpnet</li>
    <li><span class="social-dot"></span>Snapgrid</li>
  </ul>
</div>
<div class="footer-col abs" style="left:761px">
  <div class="footer-head">NEWSLETTER</div>
</div>
<div class="news-input abs">Enter mail..</div>
<div class="btn-subscribe abs">SUBSCRIBE</div>
<div class="footer-rule abs"></div>
<p class="copyright abs">@copyright 2017 Tidewell Marine.All Rights Reserved</p>

</body>
</html>
```